Executive Coaching and Spiritual Development Company needs a business card design.

We need a business card design for our company. We already have a logo that was created through Inkharbor that we will submit and would like to see this work on black, blue and white backgrounds. Our personal information should be included as well. The design should communicate trust, spirituality, support and partnership.

Industry/Entity Type

Business

Colors
0255a3
33a6d7
ffffff
000000
474747

Requirements
Nice to have
• The colors offered here are just ideas--we are open to other suggestions, too.

```html
<!DOCTYPE html>
<html lang="en">
<head>
<meta charset="utf-8">
<title>Stillwater Business Card</title>
<link rel="stylesheet" href="https://fonts.googleapis.com/css2?family=Arvo:wght@700&family=Lato:wght@400;700;900&display=swap">
<style>
  :root {
    --blue: #0255a3;
    --ink: #0f1f2a;
    --text: #222222;
    --paper: #f7f7f7;
    --stage: #2b2b2b;
    --ring: #1d2a33;
  }
  * { margin: 0; padding: 0; box-sizing: border-box; }
  html, body { width: 1200px; height: 900px; overflow: hidden; }
  body { background: var(--stage); position: relative; font-family: "Lato", sans-serif; }

  .card {
    position: absolute;
    width: 560px;
    height: 320px;
    background: var(--paper);
    overflow: hidden;
    box-shadow: 0 10px 30px rgba(0,0,0,0.45);
  }
  .card--front { left: 60px; top: 80px; }
  .card--back { left: 580px; top: 500px; }

  .card__bands { position: absolute; inset: 0; width: 560px; height: 320px; }
  .card__bands path { fill: var(--blue); }

  .brand {
    position: absolute;
    display: flex;
    align-items: center;
    gap: 16px;
  }
  .brand__mark {
    width: 64px; height: 64px;
    border: 2px solid var(--ring);
    border-radius: 50%;
    flex: none;
  }
  .brand__name {
    font-family: "Arvo", serif;
    font-weight: 700;
    font-size: 48px;
    color: var(--ink);
    letter-spacing: 0.5px;
    white-space: nowrap;
  }
  .card--front .brand { left: 110px; top: 125px; }
  .card--back .brand { left: 95px; top: 58px; }
  .card--back .brand__name { font-size: 44px; }

  .contact {
    position: absolute;
    right: 34px;
    top: 138px;
    text-align: right;
    color: var(--text);
    font-size: 14px;
    line-height: 1.6;
  }
  .contact__address {
    font-family: "Arvo", serif;
    color: var(--blue);
    font-weight: 700;
    font-size: 13px;
    line-height: 1.25;
    margin-bottom: 8px;
  }
  .contact__line { display: flex; justify-content: flex-end; align-items: center; gap: 8px; white-space: nowrap; }
  .contact__line svg { width: 14px; height: 14px; fill: var(--blue); flex: none; }
  .contact__web {
    color: var(--blue);
    font-weight: 900;
    font-size: 19px;
    margin-top: 6px;
    white-space: nowrap;
  }

  .person {
    position: absolute;
    left: 40px;
    bottom: 62px;
  }
  .person__name { color: var(--blue); font-weight: 900; font-size: 19px; letter-spacing: 0.3px; white-space: nowrap; }
  .person__role { color: var(--text); font-weight: 700; font-size: 14px; white-space: nowrap; }
</style>
</head>
<body>

<section class="card card--front" aria-label="Card front">
  <svg class="card__bands" viewBox="0 0 560 320" aria-hidden="true">
    <path d="M0 0 H560 V6 H0 Z"/>
    <path d="M0 0 H290 Q276 0 270 12 Q265 20 250 20 H0 Z"/>
    <path d="M0 314 H560 V320 H0 Z"/>
    <path d="M560 320 H300 Q312 306 326 302 H560 Z"/>
  </svg>
  <div class="brand">
    <span class="brand__mark" aria-hidden="true"></span>
    <span class="brand__name">Stillwater</span>
  </div>
</section>

<section class="card card--back" aria-label="Card back">
  <svg class="card__bands" viewBox="0 0 560 320" aria-hidden="true">
    <path d="M0 0 H560 V6 H0 Z"/>
    <path d="M560 0 H290 Q300 0 308 12 Q314 20 330 20 H560 Z"/>
    <path d="M0 314 H560 V320 H0 Z"/>
    <path d="M560 320 H220 Q232 300 252 298 H560 Z"/>
  </svg>
  <div class="brand">
    <span class="brand__mark" aria-hidden="true"></span>
    <span class="brand__name">Stillwater</span>
  </div>
  <div class="contact">
    <p class="contact__address">Harbor City, Eastvale,<br>Coastland 7310</p>
    <p class="contact__line">555-204-7716
      <svg viewBox="0 0 24 24" aria-hidden="true"><path d="M6.6 10.8a15.1 15.1 0 0 0 6.6 6.6l2.2-2.2a1 1 0 0 1 1-.25 11.4 11.4 0 0 0 3.6.6 1 1 0 0 1 1 1V20a1 1 0 0 1-1 1A17 17 0 0 1 3 4a1 1 0 0 1 1-1h3.5a1 1 0 0 1 1 1c0 1.25.2 2.45.6 3.6a1 1 0 0 1-.25 1z"/></svg>
    </p>
    <p class="contact__line">info@stillwater.example
      <svg viewBox="0 0 24 24" aria-hidden="true"><path d="M2 5h20v14H2z M3 6l9 7 9-7" fill="none" stroke="#0255a3" stroke-width="2"/></svg>
    </p>
    <p class="contact__web">www.stillwater.example</p>
  </div>
  <div class="person">
    <p class="person__name">MARCO VELLANI</p>
    <p class="person__role">Managing Director</p>
  </div>
</section>

</body>
</html>
```